Brisk Wire Services - Electrical

We need flyers for electrical services.
Areas of work include new builds, office fitouts, switchboard upgrades, installation of ceiling fans, powerpoint and downlight upgrades, home theatre and AV systems, all exterior and emergency work. Free quotes
We would like to see designs with the colour Red with a young and modern design. Licence No: 83146K must be included and call Leopold on 0418693027.

Colors
ec1f27

```html
<!DOCTYPE html>
<html lang="en">
<head>
<meta charset="utf-8">
<title>Brisk Wire Services – Electrical</title>
<link href="https://fonts.googleapis.com/css2?family=Oswald:wght@500;600&family=Lato:ital,wght@0,700;0,900;1,900&family=Roboto:wght@700&display=swap" rel="stylesheet">
<style>
  :root {
    --red: #ec1f27;
    --navy: #1a2470;
    --navy-deep: #141c5c;
    --white: #ffffff;
    --ink: #222222;
  }
  * { margin: 0; padding: 0; box-sizing: border-box; }
  html, body { width: 902px; height: 1200px; overflow: hidden; background: var(--white); }
  .flyer { position: relative; width: 902px; height: 1200px; background: var(--white); overflow: hidden; }

  .frame { position: absolute; inset: 0; }

  .worker-photo {
    position: absolute; left: 29px; top: 35px; width: 298px; height: 548px;
    background: linear-gradient(180deg, #f2a25c 0%, #3a4256 30%, #2c3348 70%, #c96a2c 100%);
    border-radius: 120px 120px 8px 8px; opacity: .9;
  }

  .brand { position: absolute; left: 370px; top: 48px; width: 450px; text-align: center;
    font-family: "Oswald", sans-serif; font-weight: 600; color: var(--navy); line-height: 1; }
  .brand__top { display: block; font-size: 104px; letter-spacing: 1px; }
  .brand__bottom { display: block; font-size: 64px; margin-top: 12px; letter-spacing: 1px; }

  .trade-band { position: absolute; left: 261px; top: 256px; width: 620px; height: 129px;
    background: var(--red); }
  .trade-band__text { position: absolute; left: 116px; top: 8px; font-family: "Oswald", sans-serif;
    font-weight: 500; font-size: 98px; line-height: 1.1; color: var(--white); letter-spacing: 1px; }

  .quote-line { position: absolute; left: 400px; top: 408px; width: 420px; text-align: center;
    font-family: "Lato", sans-serif; font-weight: 900; font-style: italic; font-size: 28px; color: var(--navy); }
  .quote-line em, .call-pill em { color: var(--red); }

  .call-pill { position: absolute; left: 361px; top: 465px; width: 478px; height: 106px;
    background: var(--navy); border-radius: 53px 0 53px 53px; }
  .call-pill__icon { position: absolute; left: 12px; top: 12px; width: 82px; height: 82px;
    border-radius: 50%; background: var(--white); }
  .call-pill__icon svg { position: absolute; left: 17px; top: 17px; }
  .call-pill__label { position: absolute; left: 156px; top: 14px; font-family: "Lato", sans-serif;
    font-style: italic; font-weight: 700; font-size: 27px; color: var(--white); }
  .call-pill__label em { font-style: italic; }
  .call-pill__number { position: absolute; left: 156px; top: 48px; font-family: "Lato", sans-serif;
    font-weight: 900; font-size: 46px; color: var(--white); letter-spacing: 1px; }

  .skyline { position: absolute; left: 416px; top: 1036px; width: 446px; height: 97px;
    background: linear-gradient(180deg, rgba(255,255,255,.15), rgba(255,255,255,.9)); }

  .services-tag { position: absolute; left: 59px; top: 655px; width: 494px; height: 54px;
    background: var(--red); border-radius: 0 27px 27px 0; font-family: "Roboto", sans-serif;
    font-weight: 700; font-size: 35px; color: var(--white); padding-left: 25px; line-height: 54px; }

  .service { position: absolute; display: flex; align-items: center; font-family: "Lato", sans-serif;
    font-weight: 700; font-size: 21px; line-height: 1.3; color: var(--white); }
  .service__icon { width: 58px; height: 58px; border-radius: 50%; background: var(--white);
    flex: none; margin-right: 27px; display: flex; align-items: center; justify-content: center; }
  .service--right .service__icon { margin-right: 32px; }

  .licence { position: absolute; left: 74px; top: 1106px; font-family: "Lato", sans-serif;
    font-weight: 900; font-size: 24px; color: var(--ink); }

  .follow { position: absolute; left: 593px; top: 1148px; display: flex; align-items: center; gap: 8px;
    font-family: "Lato", sans-serif; font-weight: 700; font-size: 16px; color: var(--red); }
  .follow__name { color: var(--ink); }
  .follow__dot { width: 14px; height: 14px; background: var(--ink); border-radius: 50%; }
</style>
</head>
<body>
<main class="flyer">
  <svg class="frame" width="902" height="1200" viewBox="0 0 902 1200" aria-hidden="true">
    <!-- red border of header -->
    <path d="M0 0 H902 V520 Q902 598 820 598 H0 Z" fill="var(--red)"/>
    <path d="M0 0 H880 V505 Q880 585 800 585 H0 Z" fill="var(--white)"/>
    <!-- navy service panel -->
    <path d="M0 618 H742 Q862 618 862 738 V1133 H416 Q300 1050 150 1052 Q60 1054 0 1070 Z" fill="var(--navy)"/>
  </svg>

  <div class="worker-photo" role="img" aria-label="Photo of an electrician in a hard hat and work uniform holding a multimeter, with an orange cable over his shoulder"></div>

  <h1 class="brand">
    <span class="brand__top">BRISK WIRE</span>
    <span class="brand__bottom">SERVICES</span>
  </h1>

  <div class="trade-band"><span class="trade-band__text">ELECTRICAL</span></div>

  <p class="quote-line">GET A <em>FREE QUOTE</em> TODAY!</p>

  <div class="call-pill">
    <div class="call-pill__icon">
      <svg width="48" height="48" viewBox="0 0 48 48" aria-hidden="true">
        <circle cx="24" cy="24" r="21" fill="none" stroke="var(--red)" stroke-width="3"/>
        <path d="M17 13c1-1 3-1 4 0l2 4c.5 1 0 2-1 3l-1 1c1 3 3 5 6 6l1-1c1-1 2-1.5 3-1l4 2c1 1 1 3 0 4l-2 2c-2 2-7 1-12-4s-6-10-4-12z" fill="var(--red)"/>
      </svg>
    </div>
    <p class="call-pill__label">CALL <em>LEOPOLD</em> ON</p>
    <p class="call-pill__number">0418693027</p>
  </div>

  <div class="skyline" role="img" aria-label="White city skyline silhouette"></div>

  <h2 class="services-tag">Areas of work include</h2>

  <ul class="service-list">
    <li class="service" style="left:74px;top:736px">
      <span class="service__icon"><svg width="30" height="30" viewBox="0 0 30 30"><rect x="6" y="8" width="18" height="20" fill="var(--red)"/><rect x="10" y="2" width="14" height="3" fill="var(--red)"/></svg></span>New builds</li>
    <li class="service" style="left:74px;top:803px">
      <span class="service__icon"><svg width="30" height="30" viewBox="0 0 30 30"><rect x="5" y="4" width="20" height="24" fill="var(--red)"/><rect x="9" y="9" width="4" height="4" fill="#fff"/><rect x="17" y="9" width="4" height="4" fill="#fff"/><rect x="9" y="17" width="4" height="4" fill="#fff"/><rect x="17" y="17" width="4" height="4" fill="#fff"/></svg></span>Office fitouts</li>
    <li class="service" style="left:74px;top:870px">
      <span class="service__icon"><svg width="32" height="28" viewBox="0 0 32 28"><rect x="2" y="2" width="28" height="24" rx="3" fill="none" stroke="var(--red)" stroke-width="3"/><circle cx="11" cy="14" r="4" fill="var(--red)"/><rect x="19" y="8" width="6" height="12" fill="var(--red)"/></svg></span>Switchboard upgrades</li>
    <li class="service" style="left:74px;top:939px">
      <span class="service__icon"><svg width="32" height="32" viewBox="0 0 32 32"><circle cx="16" cy="16" r="3" fill="var(--red)"/><path d="M16 13 L8 2 Q16 0 18 12Z M19 17 L31 20 Q28 28 18 20Z M13 18 L6 29 Q1 22 13 15Z" fill="var(--red)"/></svg></span>Installation of ceiling fans</li>

    <li class="service service--right" style="left:434px;top:736px">
      <span class="service__icon"><svg width="28" height="30" viewBox="0 0 28 30"><rect x="9" y="1" width="10" height="6" fill="var(--red)"/><path d="M3 9 H25 V22 Q14 30 3 22Z" fill="var(--red)"/></svg></span>Powerpoint and downlight<br>upgrades</li>
    <li class="service service--right" style="left:434px;top:820px">
      <span class="service__icon"><svg width="34" height="30" viewBox="0 0 34 30"><rect x="3" y="2" width="11" height="26" rx="2" fill="var(--red)"/><rect x="20" y="2" width="11" height="26" rx="2" fill="var(--red)"/><circle cx="8.5" cy="19" r="3" fill="#fff"/><circle cx="25.5" cy="19" r="3" fill="#fff"/></svg></span>Home theatre</li>
    <li class="service service--right" style="left:434px;top:890px">
      <span class="service__icon"><svg width="36" height="20" viewBox="0 0 36 20"><rect x="1" y="2" width="34" height="14" rx="2" fill="var(--red)"/><circle cx="27" cy="9" r="3" fill="#fff"/><rect x="5" y="7" width="12" height="3" fill="#fff"/></svg></span>AV systems</li>
    <li class="service service--right" style="left:434px;top:964px">
      <span class="service__icon"><svg width="30" height="32" viewBox="0 0 30 32"><rect x="9" y="1" width="3" height="8" fill="var(--red)"/><rect x="18" y="1" width="3" height="8" fill="var(--red)"/><path d="M5 9 H25 V16 Q25 24 15 24 Q5 24 5 16Z" fill="var(--red)"/><path d="M15 24 V29 H26" fill="none" stroke="var(--red)" stroke-width="3"/></svg></span>All exterior and emergency<br>work</li>
  </ul>

  <p class="licence">LICENCE NO: 83146K</p>

  <p class="follow">Follow us on : <span class="follow__dot"></span><span class="follow__name">Brisk Wire Services</span></p>
</main>
</body>
</html>
```